Need Letterhead Design & Matching Business Card

I have a logo that I love already. But the letterhead is less than appealing and boring. I'd like a design for my letterhead which I will match with business cards. Also, I'd like to have used fonts that are generally available, as my current letterhead uses a font named "SPACE" which nobody has unless they download it...so when a Word version is forwarded, it looks awful on the receiver's screed due to not having the font. That being said, modern is the look we like and are going for.

My business is "Halloran Brightmoor PC" - a law firm specializing in representing people who have suffered catastrophic injuries or death (plane, auto, train crashes etc.).

See attached letterhead, which has all of the pertinent information. My logo is also attached in various formats.

```html
<!DOCTYPE html>
<html lang="en">
<head>
<meta charset="utf-8">
<title>Halloran Brightmoor PC — Business Card</title>
<link href="https://fonts.googleapis.com/css2?family=Open+Sans:wght@300;400&display=swap" rel="stylesheet">
<style>
  :root {
    --backdrop: #ebe4df;
    --card-dark: #1d1d1d;
    --mark-dark: #3b3b3b;
    --card-light: #f8f8f6;
    --ink: #2e2e2e;
    --ink-soft: #666666;
  }
  * { margin: 0; padding: 0; box-sizing: border-box; }
  html, body {
    width: 1118px; height: 1200px; overflow: hidden;
    background: var(--backdrop);
    font-family: "Open Sans", Arial, sans-serif;
  }
  .card {
    position: absolute; left: 149px; width: 820px; height: 525px;
  }
  .card--front { top: 55px; background: var(--card-dark); }
  .card--back { top: 620px; background: var(--card-light); }

  .brand { display: flex; align-items: center; gap: 22px; }
  .brand__square { flex: none; }
  .brand__name {
    font-weight: 300; text-transform: uppercase; letter-spacing: 0.12em;
    line-height: 1.15;
  }
  .card--front .brand {
    position: absolute; left: 50%; top: 50%; transform: translate(-50%, -62%);
  }
  .card--front .brand__square { width: 110px; height: 110px; background: var(--mark-dark); }
  .card--front .brand__name { font-size: 42px; color: var(--mark-dark); }

  .card--back .brand { position: absolute; left: 69px; top: 65px; gap: 16px; }
  .card--back .brand__square { width: 80px; height: 80px; background: var(--ink); }
  .card--back .brand__name { font-size: 31px; color: var(--ink); }

  .person { position: absolute; left: 69px; top: 400px; }
  .person__name { font-size: 25px; color: var(--ink); text-transform: uppercase; line-height: 1.25; }
  .person__title { font-size: 25px; color: var(--ink-soft); font-weight: 300; line-height: 1.25; }

  .contact { position: absolute; left: 413px; top: 238px; font-size: 21px; line-height: 31px; color: var(--ink-soft); }
  .contact__firm { color: var(--ink); }
  .contact__lines { list-style: none; margin-top: 18px; }
  .contact__lines li { display: flex; align-items: center; gap: 12px; }
  .contact__lines svg { width: 20px; height: 20px; fill: var(--ink); flex: none; }
</style>
</head>
<body>
  <section class="card card--front">
    <div class="brand">
      <div class="brand__square"></div>
      <div class="brand__name">Halloran<br>Brightmoor PC</div>
    </div>
  </section>

  <section class="card card--back">
    <div class="brand">
      <div class="brand__square"></div>
      <div class="brand__name">Halloran<br>Brightmoor PC</div>
    </div>

    <div class="person">
      <p class="person__name">Daniel R. Ashcombe</p>
      <p class="person__title">Founder &amp; CEO</p>
    </div>

    <div class="contact">
      <p class="contact__firm">Halloran Brightmoor PC</p>
      <p>4820 Larchmont Ave.<br>Suite 600 Westbrook,<br>CA 90317</p>
      <ul class="contact__lines">
        <li>
          <svg viewBox="0 0 20 20" aria-hidden="true"><path d="M2 6c0-2 3-3 8-3s8 1 8 3v2h-4V6.5c-1-.5-2.5-.7-4-.7s-3 .2-4 .7V8H2zM4 10l2-3h8l2 3v7H4z"/><circle cx="10" cy="13" r="2" fill="#f8f8f6"/></svg>
          855-555-0147
        </li>
        <li>
          <svg viewBox="0 0 20 20" aria-hidden="true"><path d="M1 5h18v1.5l-9 5.5-9-5.5zM1 8.5l9 5.5 9-5.5V16H1z"/></svg>
          info@halloranbrightmoor.com
        </li>
        <li>
          <svg viewBox="0 0 20 20" aria-hidden="true"><circle cx="10" cy="10" r="8.5"/><path d="M6 5c2 0 3 2 2 3s-3 1-3 3 2 2 2 4M13 4c-1 2 1 3 3 3M12 11c2 0 3 1 2 3" stroke="#f8f8f6" stroke-width="1.4" fill="none"/></svg>
          www.halloranbrightmoor.com
        </li>
      </ul>
    </div>
  </section>
</body>
</html>
```